I am a general contractor in Portland, Or. I would like a clean and simple design layout, maybe using the "didot" font, blue and dark bronze in colors are preferred. On one side of the card, it would be nice to have a logo(attached photo) and business name(KBT Construction). I don't need my job title on the card, just some thing along the lines of "harold pike, general contractor". Thanks much.

Target Market(s)

Adults from 30-55 years old. Middle to upper class.

Industry/Entity Type

Contractor

Contact Information for Business Card

KBT Construction
Harold M. Pike
2943 NE 71st Ave.
Portland, Or. 97288
503.627.9184

Font styles to use
Other font styles liked:
• didot

Colors
3277b5
7f7f7f

Requirements
Should not have
• Too much going on.

```html
<!DOCTYPE html>
<html lang="en">
<head>
<meta charset="utf-8">
<title>KBT Construction — Business Card</title>
<link href="https://fonts.googleapis.com/css2?family=Lato:wght@400;700;900&display=swap" rel="stylesheet">
<style>
  :root {
    --backdrop: #2b2b2b;
    --card: #f7f7f7;
    --brand-blue: #3277b5;
    --ink-dark: #2e2e2e;
    --ink-grey: #7f7f7f;
  }
  html, body {
    margin: 0;
    padding: 0;
    width: 1200px;
    height: 997px;
    overflow: hidden;
    background: var(--backdrop);
    font-family: "Lato", sans-serif;
  }
  .stage {
    position: relative;
    width: 1200px;
    height: 997px;
  }
  .card {
    position: absolute;
    width: 560px;
    height: 320px;
    background: var(--card);
    box-sizing: border-box;
  }
  /* Logo side */
  .card--logo {
    left: 110px;
    top: 110px;
    display: flex;
    align-items: center;
    justify-content: center;
    gap: 22px;
  }
  .brand-dot {
    width: 46px;
    height: 46px;
    border-radius: 50%;
    background: var(--brand-blue);
  }
  .brand-name {
    font-weight: 900;
    font-size: 34px;
    letter-spacing: 0.5px;
    color: var(--ink-dark);
    text-transform: uppercase;
  }
  /* Contact side */
  .card--contact {
    left: 530px;
    top: 540px;
  }
  .mark-circle {
    position: absolute;
    left: 70px;
    top: 56px;
    width: 130px;
    height: 130px;
    border-radius: 50%;
    background: var(--brand-blue);
  }
  .card--contact .brand-name {
    position: absolute;
    left: 40px;
    bottom: 34px;
    font-size: 26px;
  }
  .contact {
    position: absolute;
    left: 290px;
    top: 48px;
    line-height: 1.2;
  }
  .contact__name {
    font-weight: 700;
    font-size: 22px;
    color: var(--brand-blue);
    margin: 0 0 2px;
  }
  .contact__role {
    font-size: 13px;
    text-transform: uppercase;
    color: var(--ink-grey);
    margin: 0 0 4px;
  }
  .contact__line {
    font-size: 16px;
    color: var(--ink-grey);
    margin: 0;
  }
</style>
</head>
<body>
  <main class="stage">
    <section class="card card--logo" aria-label="Business card, logo side">
      <span class="brand-dot" aria-hidden="true"></span>
      <span class="brand-name">KBT Construction</span>
    </section>

    <section class="card card--contact" aria-label="Business card, contact side">
      <span class="mark-circle" aria-hidden="true"></span>
      <div class="contact">
        <p class="contact__name">Harold M. Pike</p>
        <p class="contact__role">General Contractor</p>
        <p class="contact__line">503.627.9184</p>
        <p class="contact__line">pikebuilds@mailbox.net</p>
      </div>
      <span class="brand-name">KBT Construction</span>
    </section>
  </main>
</body>
</html>
```